Business cards in digital learning for freelancer

Hello, I need a business cards in french. I work in the Digital learning industries as freeelancer; I'm an expert in digital learning. I work in France. My customer are in the health industry, pharmaceutical industry, and training organization. I've got a logo. I offer three services: consulting, Design, and Training. In the consulting, I offers coaching to choose your digital learning tools and the digital learning strategy. For the Design, I product differents level of elearning like rapid-learning, elearning, micro-learning, video-learning. And for the training service, I've create training about pedagogy, digital learning management project, Digital learning design.
I join my Logo create in this platform. My universe is gamified. I like the life, and I'm very social. I want a card like I'm I. I love Art (painting), Europeen comics. I use in my visual support "permanent maker" font and caracters. I would like cards: elegant, modern, Top class. If you need any information, you can ask me.
thanks for ideas

Target Market(s)

in health industries and training organization for Training manager, instructor, human resources director

Contact Information for Business Card

Phone number : 06 31 87 59 14 , mail: lucienmervaux@postelia.fr, web: lucienmervaux.fr , LinkedIn

Font styles to use
Sans Serif

Requirements
Must have
• Use my logo and write my 3 services (consulting, training, design)

```html
<!DOCTYPE html>
<html lang="fr">
<head>
<meta charset="utf-8">
<title>Lucien Mervaux – Cartes de visite</title>
<link rel="stylesheet" href="https://fonts.googleapis.com/css2?family=Arimo:wght@400;700&family=Cinzel:wght@500&display=swap">
<style>
  :root {
    --backdrop: #2a2624;
    --card: #0d0d0d;
    --orange: #f27420;
    --grey-line: #555555;
    --text-light: #d6d6d6;
    --text-grey: #8a8a8a;
    --social-blue: #1a7bc0;
    --steel: #a8a8a8;
  }
  * { margin: 0; padding: 0; box-sizing: border-box; }
  html, body { width: 1200px; height: 842px; overflow: hidden; }
  body {
    background: var(--backdrop);
    font-family: "Arimo", Arial, sans-serif;
    position: relative;
  }
  .card {
    position: absolute;
    top: 266px;
    width: 540px;
    height: 310px;
    background: var(--card);
    overflow: hidden;
    box-shadow: 0 14px 30px rgba(0,0,0,.45);
  }
  .card--contact { left: 40px; }
  .card--brand { left: 620px; }

  /* contact side */
  .band { position: absolute; left: 0; right: 0; background: var(--orange); }
  .band--top { top: 0; height: 11px; }
  .band--bottom { bottom: 0; height: 13px; }

  .contact {
    position: absolute; inset: 0;
    display: flex; flex-direction: column; align-items: center;
    padding-top: 50px;
    text-align: center;
  }
  .contact__name {
    font-family: "Cinzel", "Trajan Pro", serif;
    font-weight: 500;
    color: var(--orange);
    font-size: 28px;
    letter-spacing: .5px;
    line-height: 1;
  }
  .contact__role {
    color: var(--text-light);
    font-size: 16px;
    margin-top: 6px;
  }
  .divider {
    display: flex; align-items: center; gap: 8px;
    width: 270px;
  }
  .divider::before, .divider::after {
    content: ""; flex: 1; height: 1px; background: var(--grey-line);
  }
  .divider--icons { margin-top: 12px; }
  .icon-box {
    width: 28px; height: 28px; border-radius: 5px;
    background: var(--orange);
    display: flex; align-items: center; justify-content: center;
  }
  .icon-box svg { width: 18px; height: 18px; }
  .contact__details {
    margin-top: 10px;
    color: var(--text-light);
    font-size: 16px;
    line-height: 20px;
    font-style: normal;
  }
  .divider--social { margin-top: 12px; width: 300px; }
  .social-dot {
    width: 26px; height: 26px; border-radius: 50%;
    background: var(--social-blue);
  }

  /* brand side */
  .tab {
    position: absolute; width: 34px; height: 50px; background: var(--orange);
  }
  .tab--left { left: 0; top: 130px; border-right: 4px solid var(--steel); }
  .tab--right { right: 0; top: 34px; border-left: 4px solid var(--steel); }
  .brand {
    position: absolute; inset: 0;
    display: flex; flex-direction: column; align-items: center;
    padding-top: 50px;
  }
  .brand__emblem {
    width: 130px; height: 82px;
    border-radius: 40px 40px 10px 10px;
    background: radial-gradient(circle at 62% 50%, #e36d1f 0 30%, #5d5a58 62%, #2b2a29 100%);
  }
  .brand__name {
    margin-top: 10px;
    font-family: "Arimo", Arial, sans-serif;
    font-weight: 700;
    color: var(--orange);
    font-size: 42px;
    letter-spacing: 3px;
    line-height: 1;
  }
  .brand__tagline {
    display: flex; align-items: center; gap: 8px;
    width: 300px; margin-top: 6px;
    font-family: "Cinzel", serif;
    font-size: 11px; letter-spacing: 1.5px;
    color: var(--text-grey);
  }
  .brand__tagline::before, .brand__tagline::after {
    content: ""; flex: 1; height: 1px; background: var(--grey-line);
  }
  .brand__services {
    margin-top: 8px;
    color: var(--text-light);
    font-size: 12.5px; letter-spacing: 1px;
    display: flex; align-items: center; gap: 8px;
  }
  .brand__services .dot {
    width: 7px; height: 7px; border-radius: 50%; background: var(--orange);
  }
</style>
</head>
<body>

<section class="card card--contact" aria-label="Recto contact">
  <div class="band band--top"></div>
  <div class="contact">
    <h1 class="contact__name">Lucien Mervaux</h1>
    <p class="contact__role">Managing Director</p>
    <div class="divider divider--icons">
      <span class="icon-box" aria-label="Téléphone">
        <svg viewBox="0 0 24 24"><path fill="#111" d="M3 9c0-3 4-5 9-5s9 2 9 5v2h-5V9c-1-.6-2.4-1-4-1s-3 .4-4 1v2H3zM7 12h10l2 7H5z"/></svg>
      </span>
      <span class="icon-box" aria-label="E-mail">
        <svg viewBox="0 0 24 24"><rect x="3" y="6" width="18" height="12" fill="none" stroke="#111" stroke-width="2"/><path d="M3 6l9 7 9-7M3 18l7-6M21 18l-7-6" fill="none" stroke="#111" stroke-width="1.6"/></svg>
      </span>
      <span class="icon-box" aria-label="Site web">
        <svg viewBox="0 0 24 24"><circle cx="12" cy="12" r="8.5" fill="none" stroke="#111" stroke-width="2"/><path d="M3.5 12h17M12 3.5c-3 3-3 14 0 17M12 3.5c3 3 3 14 0 17" fill="none" stroke="#111" stroke-width="1.5"/></svg>
      </span>
    </div>
    <address class="contact__details">
      06 31 87 59 14<br>
      lucienmervaux@postelia.fr<br>
      www.lucienmervaux.fr
    </address>
    <div class="divider divider--social">
      <span class="social-dot" aria-label="Profil professionnel"></span>
    </div>
  </div>
  <div class="band band--bottom"></div>
</section>

<section class="card card--brand" aria-label="Verso marque">
  <div class="tab tab--left"></div>
  <div class="tab tab--right"></div>
  <div class="brand">
    <div class="brand__emblem" role="img" aria-label="Emblème illustré : cerveau gris et arbre orange stylisé"></div>
    <h2 class="brand__name">MERVAUX</h2>
    <p class="brand__tagline">DIGITAL LEARNING</p>
    <p class="brand__services">CONSULTING <span class="dot"></span> TRAINING <span class="dot"></span> DESIGN</p>
  </div>
</section>

</body>
</html>
```